Law Offices business card

Hi there, I'll need business card for the Law Offices of Tobin Haskell. The information must convey his strategic approach and quick resolution to complex business litigation needs. Please emphasize Civil Litigation, Corporate Law, Business Governance and Real Estate Law. Tobin has over 25 years of experience in these fields.The card should be modern and edgy and the message should be clear. Please consult his current website for ideas.

Business

```html
<!DOCTYPE html>
<html lang="en">
<head>
<meta charset="utf-8">
<title>Law Offices of Tobin Haskell – Business Card</title>
<link rel="stylesheet" href="https://fonts.googleapis.com/css2?family=Cormorant+Garamond:wght@500;700&family=Jost:wght@400&display=swap">
<style>
  :root {
    --navy: #1f2a44;
    --navy-light: #2a3550;
    --ink: #555a63;
    --ink-dark: #4a4f58;
    --rule: #8a8f98;
    --paper: #ffffff;
    --backdrop: #d6d6d6;
  }
  * { margin: 0; padding: 0; box-sizing: border-box; }
  html, body {
    width: 1200px; height: 849px; overflow: hidden;
    background: var(--backdrop);
  }
  .canvas {
    width: 1200px; height: 849px;
    display: flex; align-items: center; justify-content: center; gap: 60px;
  }
  .card {
    width: 520px; height: 297px;
    background: var(--paper);
    position: relative;
    overflow: hidden;
  }

  /* Front */
  .card-front .name {
    position: absolute; top: 62px; left: 0; right: 0;
    text-align: center;
    font-family: "Cormorant Garamond", serif; font-weight: 500;
    font-size: 40px; letter-spacing: 2px; text-transform: uppercase;
    color: var(--navy); line-height: 1;
  }
  .card-front .title {
    position: absolute; top: 106px; left: 0; right: 0;
    text-align: center;
    font-family: "Cormorant Garamond", serif; font-weight: 700;
    font-size: 16px; letter-spacing: 2px; text-transform: uppercase;
    color: var(--navy);
  }
  .card-front .firm {
    position: absolute; top: 146px; left: 30px;
    font-family: "Cormorant Garamond", serif; font-weight: 700;
    font-size: 19px; letter-spacing: 0.5px; text-transform: uppercase;
    color: var(--navy);
  }
  .card-front .rule {
    position: absolute; top: 172px; left: 30px; right: 30px;
    height: 1px; background: var(--rule);
  }
  .contact {
    position: absolute; top: 186px; left: 30px; right: 30px;
    display: flex; justify-content: space-between;
    font-family: "Jost", sans-serif; font-size: 13.5px;
    color: var(--ink); line-height: 1.35;
  }
  .contact .phones { font-size: 16px; line-height: 1.25; }

  /* Back */
  .card-back .band {
    position: absolute; top: 0; left: 0; right: 0; height: 150px;
    background: linear-gradient(180deg, var(--navy-light) 0%, var(--navy) 100%);
  }
  .card-back .back-text {
    position: absolute; top: 164px; left: 20px; right: 20px;
    text-align: center;
    font-family: "Cormorant Garamond", serif; text-transform: uppercase;
    color: var(--ink-dark);
  }
  .back-text .firm-small {
    font-size: 13px; font-weight: 700; letter-spacing: 1px; color: var(--navy);
  }
  .back-text .practice {
    font-size: 19px; font-weight: 500; letter-spacing: 1px;
    line-height: 1.3; margin-top: 6px;
  }
  .back-text .practice + .practice { margin-top: 2px; }
  .back-text .tagline {
    margin-top: 10px;
    font-size: 13px; font-weight: 700; letter-spacing: 1.5px; color: var(--navy);
  }
</style>
</head>
<body>
<main class="canvas">
  <section class="card card-front">
    <h1 class="name">Tobin Haskell</h1>
    <p class="title">Attorney</p>
    <p class="firm">Law Offices of Tobin Haskell, P.A.</p>
    <div class="rule"></div>
    <div class="contact">
      <div class="address">118 Harbor Lane<br>Coral Bay, Florida 33901</div>
      <div class="phones">555-214-3870<br>555-308-4192</div>
      <div class="web">tobin@haskelllaw.com<br>www.haskelllaw.com</div>
    </div>
  </section>

  <section class="card card-back">
    <div class="band"></div>
    <div class="back-text">
      <p class="firm-small">Law Offices of Tobin Haskell, P.A.</p>
      <p class="practice">- Civil Litigation &nbsp;-&nbsp; Corporate Law -</p>
      <p class="practice">- Business Governance &nbsp;-&nbsp; Real Estate Law -</p>
      <p class="tagline">Strategic Approach · Quick Resolution · 25+ Years</p>
    </div>
  </section>
</main>
</body>
</html>
```